Business Card Design

Attached is my current Business card I do not like it but I must save the logo portion of it. Don't like the color or the lettering am looking for more architectural look in grays or taupe with the green more of a charturese color and the blue a charcoal color on a textured paper that looks more like something high-end that would appeal to an architect or a designer. We make concrete decorative items such as concrete fireplaces, sinks, tops and more.

Target Market(s)

Architects designers of Commercial and Residential - artistic features

Industry/Entity Type

Architect

Contact Information for Business Card

Marla T. Quinby President and Marketing Director
602-471-8836
email marla@quillstoneworks.example
Showroom "Valtique Design Center" 4128 W Larkmoor Scottsdale AZ
Fax: 602-713-4429

Font styles to use
Sans Serif

Requirements
Must have
• Architectural
Natural and earthy colors with a touch of color in the existing attached

```html
<!DOCTYPE html>
<html lang="en">
<head>
<meta charset="utf-8">
<title>Quillstone Works – Business Card</title>
<link rel="stylesheet" href="https://fonts.googleapis.com/css2?family=Orbitron:wght@400;500&display=swap">
<style>
  :root {
    --taupe-light: #b3a999;
    --taupe: #a0968a;
    --taupe-deep: #8c8377;
    --skyline: #6f675d;
    --charcoal: #2e3032;
    --charcoal-deep: #26282a;
    --chartreuse: #b3cf2d;
    --chartreuse-deep: #6f8a0e;
    --paper-light: #e6dfd2;
    --ink: #2a2c2e;
    --divider: #7d9421;
    --icon-grey: #b9b2a6;
  }
  * { margin: 0; padding: 0; box-sizing: border-box; }
  html, body {
    width: 1200px;
    height: 702px;
    overflow: hidden;
    background: var(--taupe);
  }
  .card {
    position: relative;
    width: 1200px;
    height: 702px;
    overflow: hidden;
    font-family: "Orbitron", sans-serif;
    text-transform: uppercase;
    background-color: var(--taupe);
    background-image:
      radial-gradient(circle at 2px 3px, rgba(255,255,255,0.16) 0.8px, transparent 1.4px),
      radial-gradient(circle at 5px 1px, rgba(60,52,42,0.14) 0.8px, transparent 1.4px),
      linear-gradient(180deg, var(--taupe-light) 0%, var(--taupe) 45%, var(--taupe-deep) 100%);
    background-size: 7px 7px, 9px 9px, 100% 100%;
  }
  .skyline {
    position: absolute;
    left: 77px;
    top: 103px;
    width: 415px;
    height: 367px;
    background: linear-gradient(180deg, #7a7267 0%, var(--skyline) 100%);
  }
  .brand {
    position: absolute;
    right: 77px;
    top: 108px;
    display: flex;
    align-items: center;
    gap: 14px;
    color: var(--chartreuse-deep);
    font-size: 30px;
    font-weight: 500;
    letter-spacing: 3px;
  }
  .brand-square {
    width: 22px;
    height: 22px;
    background: var(--charcoal);
  }
  .name {
    position: absolute;
    right: 77px;
    top: 216px;
    color: var(--charcoal);
    font-size: 46px;
    font-weight: 400;
    letter-spacing: 6.5px;
    white-space: nowrap;
  }
  .title {
    position: absolute;
    right: 73px;
    top: 290px;
    color: var(--chartreuse-deep);
    font-size: 21.5px;
    font-weight: 500;
    letter-spacing: 5px;
    white-space: nowrap;
  }
  .contact-band {
    position: absolute;
    left: 0;
    top: 470px;
    width: 1200px;
    height: 105px;
    background: linear-gradient(180deg, #37393b 0%, var(--charcoal-deep) 40%);
  }
  .contact {
    position: absolute;
    display: flex;
    align-items: center;
    gap: 18px;
    color: var(--paper-light);
    font-size: 21px;
    letter-spacing: 2.4px;
    white-space: nowrap;
  }
  .contact-email { left: 77px; top: 505px; }
  .contact-phone { right: 77px; top: 500px; gap: 24px; font-size: 23px; }
  .footer-band {
    position: absolute;
    left: 0;
    top: 575px;
    width: 1200px;
    height: 127px;
    background: var(--chartreuse);
    color: var(--ink);
  }
  .footer-divider {
    position: absolute;
    left: 707px;
    top: 13px;
    width: 1px;
    height: 103px;
    background: var(--divider);
  }
  .footer-label {
    position: absolute;
    display: flex;
    align-items: center;
    gap: 14px;
    font-size: 19px;
    letter-spacing: 2.5px;
  }
  .fax-label { left: 492px; top: 22px; }
  .showroom-label { right: 70px; top: 20px; }
  .footer-detail {
    position: absolute;
    font-size: 13.5px;
    letter-spacing: 2px;
    line-height: 23px;
    white-space: nowrap;
  }
  .fax-number { left: 482px; top: 94px; }
  .showroom-address { right: 70px; top: 71px; text-align: right; }
</style>
</head>
<body>
<div class="card">
  <div class="skyline" role="img" aria-label="Skyline illustration: tall office tower, slim spired building and small house with lit windows"></div>

  <div class="brand"><span class="brand-square"></span>Quillstone Works</div>

  <h1 class="name">Marla T. Quinby</h1>
  <p class="title">President and Marketing Director</p>

  <div class="contact-band"></div>

  <div class="contact contact-email">
    <svg width="61" height="40" viewBox="0 0 61 40" aria-hidden="true">
      <rect x="1" y="1" width="59" height="38" fill="var(--icon-grey)" stroke="#e6dfd2" stroke-width="2"/>
      <polyline points="1,1 30.5,24 60,1" fill="none" stroke="#3a3c3e" stroke-width="2"/>
      <line x1="1" y1="39" x2="24" y2="19" stroke="#3a3c3e" stroke-width="2"/>
      <line x1="37" y1="19" x2="60" y2="39" stroke="#3a3c3e" stroke-width="2"/>
    </svg>
    <span>marla@quillstoneworks.example</span>
  </div>

  <div class="contact contact-phone">
    <svg width="52" height="51" viewBox="0 0 52 51" aria-hidden="true">
      <rect x="0" y="0" width="52" height="51" rx="7" fill="var(--icon-grey)"/>
      <path d="M17 10 c-4 2 -6 5 -5 9 c2 9 9 18 18 22 c4 1 7 -1 9 -5 l-6 -5 c-2 1 -3 2 -5 1 c-4 -2 -7 -6 -8 -10 c0 -2 1 -3 3 -4 z" fill="#26282a"/>
    </svg>
    <span>602-471-8836</span>
  </div>

  <footer class="footer-band">
    <div class="footer-divider"></div>

    <div class="footer-label fax-label">
      <svg width="42" height="29" viewBox="0 0 42 29" aria-hidden="true">
        <rect x="1" y="1" width="40" height="27" fill="none" stroke="var(--ink)" stroke-width="2"/>
        <polyline points="1,1 21,17 41,1" fill="none" stroke="var(--ink)" stroke-width="2"/>
        <line x1="1" y1="28" x2="16" y2="13" stroke="var(--ink)" stroke-width="2"/>
        <line x1="26" y1="13" x2="41" y2="28" stroke="var(--ink)" stroke-width="2"/>
      </svg>
      <span>Fax</span>
    </div>
    <p class="footer-detail fax-number">602-713-4429</p>

    <div class="footer-label showroom-label">
      <svg width="42" height="38" viewBox="0 0 42 38" aria-hidden="true">
        <polygon points="21,2 40,17 2,17" fill="none" stroke="var(--ink)" stroke-width="2"/>
        <rect x="6" y="17" width="30" height="19" fill="none" stroke="var(--ink)" stroke-width="2"/>
        <rect x="10" y="21" width="7" height="7" fill="var(--ink)"/>
        <rect x="25" y="21" width="7" height="7" fill="var(--ink)"/>
        <rect x="18" y="24" width="6" height="12" fill="var(--ink)"/>
        <rect x="28" y="5" width="4" height="8" fill="var(--ink)"/>
      </svg>
      <span>Showroom</span>
    </div>
    <p class="footer-detail showroom-address">Valtique Design Center<br>4128 W Larkmoor Scottsdale AZ</p>
  </footer>
</div>
</body>
</html>
```